Health Spectrum and Energy Slides

Create beautiful and facinating PowerPoint slides that inspire and motivate

Target Market(s)

Clients looking for strategic breakthroughs and transformation

Industry/Entity Type

Health

Requirements
Must have
• Beautiful, heartfelt and fascinating graphics.
Nice to have
• Award winning designs.

```html
<!DOCTYPE html>
<html lang="en">
<head>
<meta charset="UTF-8">
<title>Seasons Slide</title>
<link rel="stylesheet" href="https://fonts.googleapis.com/css2?family=Montserrat:wght@700&family=Arimo:wght@400;700&display=swap">
<style>
  :root {
    --page-bg: #f7f7f7;
    --title-grey: #b3babd;
    --frame: #dcdcdc;
    --label-grey: #8a8f92;
    --ink-dark: #0c0c0c;
    --ink-light: #ffffff;
    --sky-band: rgba(84, 118, 206, 0.78);
  }
  * { margin: 0; padding: 0; box-sizing: border-box; }
  html, body {
    width: 1200px;
    height: 746px;
    overflow: hidden;
    background: var(--page-bg);
  }
  .board {
    position: relative;
    width: 1200px;
    height: 746px;
  }
  .board-title {
    position: absolute;
    top: 88px;
    left: 0;
    width: 1200px;
    text-align: center;
    font-family: "Montserrat", sans-serif;
    font-weight: 700;
    font-size: 113px;
    line-height: 1;
    letter-spacing: 1px;
    color: var(--title-grey);
  }
  .slide {
    position: absolute;
    top: 298px;
    width: 555px;
    height: 324px;
    border: 2px solid var(--frame);
    background: #fff;
    overflow: hidden;
    font-family: "Arimo", Arial, sans-serif;
    text-align: center;
  }
  .slide--diagonal { left: 16px; }
  .slide--columns { left: 600px; }
  .slide-photo {
    position: absolute;
    inset: 0;
  }
  .slide--diagonal .slide-photo {
    background: linear-gradient(135deg,
      #3fae2a 0%, #8cc43a 16%, #f0d35a 30%, #f4c64a 44%,
      #f2a23a 55%, #e46a1c 66%, #35b9d4 74%, #2ec0dc 88%, #5fd2e6 100%);
  }
  .slide--columns .slide-photo {
    background: linear-gradient(90deg,
      #d98fc0 0%, #e6a6cf 22%, #9cce3a 28%, #86c22e 47%,
      #f2c23a 53%, #eab53a 72%, #e8ecec 78%, #f4f6f6 100%);
  }
  .slide-heading {
    position: absolute;
    left: 0;
    width: 100%;
    font-weight: 700;
    line-height: 1;
  }
  .slide-body {
    position: absolute;
    left: 0;
    width: 100%;
    font-weight: 400;
  }
  .slide--diagonal .slide-heading {
    top: 84px;
    font-size: 26px;
    color: var(--ink-dark);
  }
  .slide--diagonal .slide-body {
    top: 148px;
    padding: 0 80px;
    font-size: 25px;
    line-height: 33px;
    color: var(--ink-dark);
  }
  .sky-band {
    position: absolute;
    left: 0;
    top: 96px;
    width: 100%;
    height: 136px;
    background: var(--sky-band);
  }
  .slide--columns .slide-heading {
    top: 110px;
    font-size: 21px;
    color: var(--ink-light);
  }
  .slide--columns .slide-body {
    top: 162px;
    padding: 0 70px;
    font-size: 21px;
    line-height: 28px;
    color: var(--ink-light);
  }
  .slide-number {
    position: absolute;
    top: 630px;
    font-family: "Montserrat", sans-serif;
    font-weight: 700;
    font-size: 15px;
    color: var(--label-grey);
  }
  .slide-number--first { left: 18px; }
  .slide-number--second { left: 603px; }
</style>
</head>
<body>
  <main class="board">
    <h1 class="board-title">SEASONS SLIDE</h1>

    <section class="slide slide--diagonal">
      <div class="slide-photo" role="img" aria-label="Forest photo split into diagonal bands of spring green, summer yellow, autumn orange and icy winter blue"></div>
      <h2 class="slide-heading">BE THE SKY</h2>
      <p class="slide-body">The sky has room for all types of changing weather and all the seasons.</p>
    </section>
    <span class="slide-number slide-number--first">1</span>

    <section class="slide slide--columns">
      <div class="slide-photo" role="img" aria-label="Four vertical photos looking up tree trunks: pink blossom, green leaves, yellow autumn leaves and snowy winter branches"></div>
      <div class="sky-band"></div>
      <h2 class="slide-heading">BE THE SKY</h2>
      <p class="slide-body">The sky has room for all types of changing weather and all the seasons.</p>
    </section>
    <span class="slide-number slide-number--second">2</span>
  </main>
</body>
</html>
```